findnearhub.org - creative brochure
findnearhub.org
Visit our website - findnearhub.org
Internet Services
Brick and mortar local businesses
The brochure needs to demonstrate confidence, affordability, and exclusivity.
The text for the brochure can be found on the website findnearhub.org
The design can be a 3 fold or rack card style… whatever turns out best

```html
<!DOCTYPE html>
<html lang="en">
<head>
<meta charset="utf-8">
<title>findnearhub.org – Brochure</title>
<link href="https://fonts.googleapis.com/css2?family=Open+Sans:wght@400;600;700;800&family=Oswald:wght@500;700&display=swap" rel="stylesheet">
<style>
:root{
  --red:#d9252b;
  --red-dark:#a8161b;
  --ink:#2e2e2e;
  --grey:#6b6b6b;
  --soft:#eeeeee;
  --bar:#3a3a3a;
  --stage:#d6d6d6;
  --white:#ffffff;
}
*{margin:0;padding:0;box-sizing:border-box}
html,body{width:1200px;height:600px;overflow:hidden;background:var(--stage);font-family:"Open Sans",Arial,sans-serif;color:var(--ink)}
.canvas{display:flex;gap:14px;padding:12px 8px;height:600px}
.sheet{flex:1;display:grid;grid-template-columns:repeat(3,1fr);background:var(--white);box-shadow:0 1px 4px rgba(0,0,0,.25)}
.panel{position:relative;padding:10px 11px;overflow:hidden;font-size:6.6px;line-height:1.45}
.panel + .panel{border-left:1px solid #e2e2e2}
p{color:var(--grey);margin-bottom:5px}
.red{color:var(--red)}
/* panel 1 */
.benefits{background:linear-gradient(180deg,#fafafa,#e9e9e9)}
.benefit{margin-bottom:22px}
.pin{width:34px;height:42px;display:block;margin:4px 0 4px}
.benefit h3{font-size:13px;font-weight:700;color:var(--ink)}
.benefit h4{font-size:8.5px;font-weight:700;color:var(--red);margin-bottom:3px}
/* panel 2 */
.domination h2{font-family:"Oswald",sans-serif;color:var(--red);font-size:15.5px;line-height:1.15;text-align:center;margin:14px 0 12px}
.art{border-radius:2px}
.solution-art{height:180px;background:linear-gradient(160deg,#f2f2f2,#bcbcbc 60%,#8a8a8a);margin-bottom:22px}
.brand{display:flex;align-items:center;gap:6px;justify-content:center}
.brand-dot{width:20px;height:20px;border-radius:50%;background:var(--red);flex:none}
.brand-name{font-weight:800;font-size:17px;color:var(--ink)}
.tagline{text-align:center;color:var(--red);font-size:6.5px;margin-top:2px}
.contact{text-align:center;font-size:7px;color:var(--ink);margin-top:14px;line-height:1.6}
/* panel 3 */
.stat{background:var(--white)}
.stat h2{font-family:"Oswald",sans-serif;font-size:21px;line-height:1.1;color:var(--ink);margin:8px 0 0}
.stat h2 .red{font-size:30px;display:block}
.stat h2 .small{font-size:17px}
.map-art{height:270px;margin:10px -11px 22px;background:linear-gradient(180deg,#f4f4f4,#cfcfcf 70%,#9d9d9d)}
/* bars */
.bar{background:var(--red);color:var(--white);font-weight:700;font-size:7.5px;padding:4px 7px;margin:6px -11px 6px;text-transform:uppercase}
.bar.dark{background:var(--bar)}
.checks{list-style:none;margin-bottom:6px}
.checks li{display:flex;align-items:center;gap:5px;font-size:6.4px;font-weight:700;color:var(--ink);margin-bottom:4px;text-transform:uppercase}
.checks svg{width:9px;height:9px;flex:none}
.intro{display:flex;gap:8px;margin-bottom:5px}
.phone-art{width:70px;height:92px;flex:none;background:linear-gradient(160deg,#eee,#9a9a9a)}
.search-art{height:90px;margin:-10px -11px 0;background:linear-gradient(180deg,#f7f7f7,#dedede)}
.pins-art{height:70px;margin-bottom:4px;background:linear-gradient(180deg,#fdfdfd,#d4d4d4)}
.feat{list-style:none}
.feat li{font-size:6.2px;color:var(--ink);margin-bottom:1.5px}
.feat li::before{content:"▪ ";color:var(--red)}
.guarantee-head{display:flex;align-items:flex-start;gap:6px}
.guarantee-head .bar{flex:1;margin-left:-11px;margin-right:0}
.stamp-art{width:60px;height:56px;border-radius:50%;background:radial-gradient(circle,#e8e8e8,#a9a9a9);flex:none}
.bar-lg{font-size:11px;padding:6px 8px}
.houses{position:absolute;left:11px;right:11px;bottom:12px;height:40px;background:linear-gradient(180deg,#fff,#d0d0d0)}
</style>
</head>
<body>
<main class="canvas">
  <!-- outside sheet -->
  <section class="sheet">
    <article class="panel benefits">
      <div class="benefit">
        <svg class="pin" viewBox="0 0 34 42"><path d="M17 41C17 41 2 24 2 15a15 15 0 0 1 30 0c0 9-15 26-15 26z" fill="var(--red)"/><circle cx="17" cy="15" r="9" fill="#fff"/><text x="17" y="20" text-anchor="middle" font-size="13" font-weight="700" fill="var(--red)" font-family="Open Sans,sans-serif">1</text></svg>
        <h3>Local Exposure</h3>
        <h4>Guaranteed local exposure!</h4>
        <p>The ROI (return on investment) for your business will be visible on day one – we place your listing in front of local buyers.</p>
      </div>
      <div class="benefit">
        <svg class="pin" viewBox="0 0 34 42"><path d="M17 41C17 41 2 24 2 15a15 15 0 0 1 30 0c0 9-15 26-15 26z" fill="var(--red)"/><circle cx="17" cy="15" r="9" fill="#fff"/><text x="17" y="20" text-anchor="middle" font-size="13" font-weight="700" fill="var(--red)" font-family="Open Sans,sans-serif">2</text></svg>
        <h3>Target Customers</h3>
        <h4>New local customers!</h4>
        <p>Your listings will be optimized "Locally" in the search engines, and therefore generate high quality traffic.</p>
      </div>
      <div class="benefit">
        <svg class="pin" viewBox="0 0 34 42"><path d="M17 41C17 41 2 24 2 15a15 15 0 0 1 30 0c0 9-15 26-15 26z" fill="var(--red)"/><circle cx="17" cy="15" r="9" fill="#fff"/><text x="17" y="20" text-anchor="middle" font-size="13" font-weight="700" fill="var(--red)" font-family="Open Sans,sans-serif">3</text></svg>
        <h3>We Do The Work</h3>
        <h4>We do ALL the work!</h4>
        <p>No more headaches with expensive, time consuming management of campaigns and advertising strategies.</p>
      </div>
    </article>

    <article class="panel domination">
      <h2>Local Search Domination<br>The Key To Your Success</h2>
      <div class="art solution-art" role="img" aria-label="Puzzle pieces forming the word solution"></div>
      <div class="brand"><span class="brand-dot"></span><span class="brand-name">findnearhub.org</span></div>
      <div class="tagline">Helping Businesses Grow – Locally</div>
      <div class="contact">
        findnearhub.org<br>
        1420 Harbor Lane, Millbrook, ON K0L 2V0<br>
        Tel: 555-014-2288
      </div>
    </article>

    <article class="panel stat">
      <h2>Over 80% of<span class="red">local searches</span><span class="small">turn into business</span></h2>
      <div class="art map-art" role="img" aria-label="Businessman standing on a city map with red location pins"></div>
      <div class="brand"><span class="brand-dot"></span><span class="brand-name">findnearhub.org</span></div>
      <div class="tagline">Helping Businesses Grow – Locally</div>
    </article>
  </section>

  <!-- inside sheet -->
  <section class="sheet">
    <article class="panel">
      <div class="intro">
        <div class="art phone-art" role="img" aria-label="Smartphone showing a map with a location pin"></div>
        <p>As the internet evolves and web users become more sophisticated, local consumers are turning more and more to the internet to find products and services on a local basis.</p>
      </div>
      <p>We'll get your website listed in the leading map and local directories for searches by local visitors. Everytime a local consumer searches for your product or service, you'll be there as perfect choice.</p>
      <div class="bar">We can help your business...</div>
      <ul class="checks">
        <li><svg viewBox="0 0 10 10"><rect width="10" height="10" fill="var(--red)"/><path d="M2 5l2 2 4-4" stroke="#fff" stroke-width="1.4" fill="none"/></svg>Eliminate pay per click charges</li>
        <li><svg viewBox="0 0 10 10"><rect width="10" height="10" fill="var(--red)"/><path d="M2 5l2 2 4-4" stroke="#fff" stroke-width="1.4" fill="none"/></svg>Enhance your local search presence</li>
        <li><svg viewBox="0 0 10 10"><rect width="10" height="10" fill="var(--red)"/><path d="M2 5l2 2 4-4" stroke="#fff" stroke-width="1.4" fill="none"/></svg>Reduce your advertising budget</li>
        <li><svg viewBox="0 0 10 10"><rect width="10" height="10" fill="var(--red)"/><path d="M2 5l2 2 4-4" stroke="#fff" stroke-width="1.4" fill="none"/></svg>Increase profits</li>
        <li><svg viewBox="0 0 10 10"><rect width="10" height="10" fill="var(--red)"/><path d="M2 5l2 2 4-4" stroke="#fff" stroke-width="1.4" fill="none"/></svg>Acquire new customers</li>
        <li><svg viewBox="0 0 10 10"><rect width="10" height="10" fill="var(--red)"/><path d="M2 5l2 2 4-4" stroke="#fff" stroke-width="1.4" fill="none"/></svg>Gain visibility over your competition</li>
      </ul>
      <div class="bar">Our services</div>
      <p>We specialize in getting localized results in the search engines, so if you are an Appliance Repair company in Millbrook, ON you will rank #1. Our SEO experts optimize your business presence, and have it found by local consumers searching specifically for products or services.</p>
    </article>

    <article class="panel">
      <div class="search-art" role="img" aria-label="Search box with a magnifying glass and the word search"></div>
      <div class="bar dark bar-lg">Search + Local</div>
      <p>Optimizing your local listings and seeking to be at the top of local keyword searches is essential to your business!</p>
      <p>It's how phones ring and how they find your business. With help from FINDNEARHUB.org you are sure that the best ROI dollars are spent where they really make a difference.</p>
      <p class="red"><b>We want to help you to get your local listing to the top of local search queries no matter where your local business is located.</b></p>
      <p class="red"><b>Order our services today for guaranteed results.</b></p>
      <div class="art pins-art" role="img" aria-label="Street map with red location pins"></div>
      <div class="bar">Features</div>
      <ul class="feat">
        <li>Complete Website SEO Analysis</li>
        <li>Map and directory local listings</li>
        <li>Website hosting and maintenance</li>
        <li>Directory listings, NAP citations</li>
        <li>Keyword research and ranking report</li>
        <li>Local Business Reviews</li>
        <li>Social media management</li>
        <li>Customer lead tracking</li>
        <li>Phone call tracking</li>
        <li>Photos gallery and video</li>
        <li>Monthly progress reports</li>
      </ul>
    </article>

    <article class="panel">
      <div class="guarantee-head">
        <div class="bar bar-lg">Our guarantee</div>
        <div class="stamp-art" role="img" aria-label="Guarantee seal badge"></div>
      </div>
      <p>We guarantee that our services are offered at an exclusive price level. We will not take on clients in a competing business that operate in the same geographical area. We will NEVER charge a separate retainer fee for your local placement.</p>
      <div class="bar dark bar-lg">Location, Location</div>
      <p>In the brick and mortar world it has always been about LOCATION.</p>
      <p>You can now dominate the location battle on a digital level to capture those new targeted and hot prospects ahead of your competition!</p>
      <p>We know how to get your local listings on the top of search queries no matter where your local business is located.</p>
      <p class="red"><b>Order our exclusive services today for guaranteed results!</b></p>
      <div class="houses" role="img" aria-label="Row of small house icons with a location pin"></div>
    </article>
  </section>
</main>
</body>
</html>
```